KTR Engineering Business Card Design

We’re looking for an elegant, clean, and timeless business card design that communicates experience, capability, and reliability.

KTR Engineering was established in 1995 , we are a Government Contracting company providing Professional Services to the Ministry of Harbor Works, Frontier Stewardship and the Waypoint Consortium. Our capabilities include: Acquisition & Program Management; Intelligence & Security Operations; Cyber, IT & Network Operations; Lifecycle Logistics & Asset Readiness; C5ISR Systems Engineering & Sustainment.

We want the card to reflect a straightforward, confident approach to business. The design should feel polished and professional without being flashy or overly corporate.

Design Direction
Clean, sophisticated, and uncluttered
Elegant but understated
Strong typography and thoughtful spacing
A timeless aesthetic rather than something overly trendy
Confident and established, with a sense of substance
Easy to read and practical in a real-world business setting

The overall impression should be: “These are experienced professionals who know what they’re doing, do what they say, and can be relied upon.”

We’re open to creative interpretations. The finished card should feel distinctive through its typography, proportions, layout, and attention to detail rather than through excessive graphics or visual effects.

We’re looking for a design that would make a potential client immediately feel that they’re dealing with a capable, trustworthy, and established company.

Company Colors: Navy and Gold/Yellow (but you do not need to use these colors on the card)
Company Name: KTR Engineering Associates, Inc. (known as KTR Engineering)
Website: ktrengineering.example
Company Logo: Navy & Gold (other variations attached)

```html
<!DOCTYPE html>
<html lang="en">
<head>
<meta charset="utf-8">
<title>KTR Engineering – Business Card</title>
<link rel="stylesheet" href="https://fonts.googleapis.com/css2?family=Montserrat:wght@400;500;700;800&display=swap">
<style>
  :root {
    --backdrop: #2b2b2b;
    --card-yellow: #f9e24c;
    --mark-yellow: #b8a136;
    --card-black: #141414;
    --accent-yellow: #f2dc32;
    --text-white: #ffffff;
  }
  * { box-sizing: border-box; margin: 0; padding: 0; }
  html, body {
    width: 1200px; height: 875px; overflow: hidden;
    background: var(--backdrop);
    font-family: "Montserrat", Arial, sans-serif;
  }
  .sheet {
    width: 1200px; height: 875px;
    display: flex; flex-direction: column;
    align-items: center; justify-content: center; gap: 48px;
  }
  .card {
    width: 660px; height: 377px;
    border-radius: 22px;
    position: relative; overflow: hidden;
  }
  .card--front {
    background: var(--card-yellow);
    display: flex; align-items: center; justify-content: center;
  }
  .front-wordmark {
    font-weight: 800; font-size: 150px; letter-spacing: -2px;
    color: var(--mark-yellow); line-height: 1;
  }
  .card--back {
    background: var(--card-black);
    display: flex; align-items: center;
    padding: 0 44px 0 70px;
  }
  .back-wordmark {
    width: 230px;
    font-weight: 800; font-size: 84px; letter-spacing: -1px;
    color: var(--text-white); line-height: 1;
  }
  .divider {
    width: 2px; height: 220px;
    background: var(--accent-yellow);
    margin: 0 34px 0 24px;
  }
  .details { color: var(--text-white); }
  .details__name {
    color: var(--accent-yellow);
    font-weight: 700; font-size: 26px; letter-spacing: 1px;
    text-transform: uppercase;
  }
  .details__title { font-size: 15px; margin-top: 4px; }
  .details__address { font-size: 15px; line-height: 1.45; margin-top: 18px; }
  .contact-list { list-style: none; margin-top: 18px; font-size: 15px; }
  .contact-list li { display: flex; align-items: center; gap: 10px; line-height: 1.65; }
  .contact-list svg { width: 14px; height: 14px; fill: var(--accent-yellow); flex: none; }
</style>
</head>
<body>
<main class="sheet">
  <section class="card card--front" aria-label="Card front">
    <span class="front-wordmark">KTR</span>
  </section>

  <section class="card card--back" aria-label="Card back">
    <span class="back-wordmark">KTR</span>
    <span class="divider"></span>
    <div class="details">
      <p class="details__name">Mara Velkon</p>
      <p class="details__title">Managing Director</p>
      <p class="details__address">1840 Harborline Avenue, Suite<br>310, Port Alder, VA 20000</p>
      <ul class="contact-list">
        <li>
          <svg viewBox="0 0 16 16" aria-hidden="true"><path d="M3.5 1.5l2.5 3-1.5 1.8a9 9 0 0 0 5.2 5.2L11.5 10l3 2.5-1.3 2.2c-.4.6-1.2.9-1.9.7C6.5 14 2 9.5.6 4.7.4 4 .7 3.2 1.3 2.8z"/></svg>
          555-010-4821
        </li>
        <li>
          <svg viewBox="0 0 16 16" aria-hidden="true"><path d="M1 3h14v10H1z M1.8 3.8L8 8.8l6.2-5" fill="var(--accent-yellow)"/><path d="M1.5 3.5L8 8.5l6.5-5" stroke="#141414" stroke-width="1.2" fill="none"/></svg>
          info@ktrengineering.example
        </li>
        <li>
          <svg viewBox="0 0 16 16" aria-hidden="true"><circle cx="8" cy="8" r="7"/><path d="M1 8h14M8 1c-3 3.5-3 10.5 0 14M8 1c3 3.5 3 10.5 0 14" stroke="#141414" stroke-width="1" fill="none"/></svg>
          ktrengineering.example
        </li>
      </ul>
    </div>
  </section>
</main>
</body>
</html>
```